Musical Instrument Store Needs Band Instrument Postcard to Upgrade Current Customers

We need a new postcard design to mail to our current instrument rental customers. People start out renting a student line/beginner instrument and we want to emphasize our upgrade program that allows them to apply the equity from their beginner instrument to an intermediate or professional instrument. I have attached an image of the front (Harvey Postcard Front) and back (Harvey Postcard Back) of what we have used in the past. The back still needs to have all the information currently on it. The front can be whatever you come up with (I don't necessarily care for our current design), but should include the tagline "Reach Your Full Potential". Also, if there is more room on the front or back, it would be nice to have a brief mention of our lesson studio (I have also included our lesson studio postcard for ideas).

There are also pictures of each instrument attached. There are a few for the trumpet so you can decide which one would work best.

Target Market(s)

Current instrument rental customers

Industry/Entity Type

Store

Requirements
Must have
• The back of postcard must have all the information from the file "Harvey Postcard Back". The front should have the tagline "Reach Your Full Potential". Pictures of the instruments should be on the front as well.
Nice to have
• A brief mention or reminder that we have a large lesson studio with highly qualified instructors.

```html
<!DOCTYPE html>
<html lang="en">
<head>
<meta charset="utf-8">
<title>Marcato Music Center – Harvey Upgrade Postcard</title>
<link href="https://fonts.googleapis.com/css2?family=Jost:wght@400;600;700&family=Dancing+Script:wght@400;600&family=Roboto+Condensed:wght@500&display=swap" rel="stylesheet">
<style>
  :root {
    --page-bg: #e9e7e4;
    --card-white: #ffffff;
    --ink: #111111;
    --sky-light: #eef4ff;
    --sky-blue: #6f9de0;
    --sky-violet: #5a4fa8;
    --sky-deep: #3e3a8c;
    --title-white: #ffffff;
    --lesson-panel: #efebe8;
    --badge: #111111;
  }
  * { margin: 0; padding: 0; box-sizing: border-box; }
  html, body { width: 1200px; height: 1000px; overflow: hidden; background: var(--page-bg); }
  .canvas { position: relative; width: 1200px; height: 1000px; }

  /* Front */
  .postcard-front {
    position: absolute; left: 68px; top: 34px; width: 694px; height: 443px; overflow: hidden;
    background:
      radial-gradient(ellipse 60% 45% at 52% 22%, var(--sky-light) 0%, rgba(238,244,255,0.6) 35%, rgba(238,244,255,0) 70%),
      linear-gradient(180deg, #9fc0ee 0%, var(--sky-blue) 35%, var(--sky-violet) 75%, var(--sky-deep) 100%);
  }
  .instrument-photo { position: absolute; border-radius: 40px;
    background: radial-gradient(ellipse at center, rgba(196,170,110,0.55), rgba(120,120,140,0.25) 60%, rgba(120,120,140,0) 80%); }
  .instrument-photo.left { left: 0; top: 30px; width: 275px; height: 385px; }
  .instrument-photo.right { left: 440px; top: 28px; width: 250px; height: 360px; }
  .brand-front {
    position: absolute; left: 250px; top: 26px; width: 184px;
    font-family: "Jost", sans-serif; font-weight: 700; font-size: 22px; line-height: 1.05;
    color: var(--ink); text-align: center;
  }
  .front-title {
    position: absolute; left: 0; width: 742px; top: 258px; text-align: center;
    font-family: "Dancing Script", cursive; font-weight: 400; font-size: 86px; color: var(--title-white);
    text-shadow: 0 2px 6px rgba(40,30,90,0.35);
  }
  .front-tagline {
    position: absolute; left: 0; width: 602px; top: 356px; text-align: center;
    font-family: "Roboto Condensed", sans-serif; font-weight: 500; font-size: 21px; color: var(--title-white);
  }
  .front-invite {
    position: absolute; left: 70px; width: 570px; top: 392px; text-align: center;
    font-family: "Dancing Script", cursive; font-size: 24px; color: var(--title-white);
  }

  /* Back */
  .postcard-back {
    position: absolute; left: 404px; top: 510px; width: 690px; height: 444px;
    background: var(--card-white); color: var(--ink); font-family: "Jost", sans-serif;
  }
  .brand-back {
    position: absolute; left: 32px; top: 30px; width: 200px;
    font-weight: 700; font-size: 24px; line-height: 1.05; color: var(--ink);
  }
  .contact-list { position: absolute; left: 249px; top: 21px; list-style: none; font-size: 14.5px; }
  .contact-list li { display: flex; align-items: center; gap: 9px; height: 19.5px; }
  .contact-list svg { width: 13px; height: 13px; flex: none; }
  .postage-box {
    position: absolute; left: 599px; top: 10px; width: 83px; height: 95px;
    border: 1px solid #555; text-align: center; font-size: 8.5px; line-height: 13.5px; padding-top: 8px;
    letter-spacing: 0.2px;
  }
  .postage-box strong { font-size: 10px; }
  .offer-copy {
    position: absolute; left: 27px; top: 109px; width: 246px;
    font-size: 13.4px; line-height: 19px; text-align: justify; text-align-last: left;
  }
  .call-to-action {
    position: absolute; left: 27px; top: 228px; width: 246px; text-align: center;
    font-weight: 600; font-size: 13.4px; line-height: 18px;
  }
  .lesson-panel {
    position: absolute; left: 27px; top: 311px; width: 252px; height: 112px; background: var(--lesson-panel);
  }
  .lesson-badge { position: absolute; left: 8px; top: -24px; width: 96px; height: 96px; }
  .lesson-headline {
    position: absolute; left: 114px; top: 10px; width: 132px;
    font-weight: 600; font-size: 13.4px; line-height: 18px;
  }
  .lesson-list {
    position: absolute; left: 0; width: 252px; top: 78px; text-align: center;
    font-size: 10px; line-height: 14px;
  }
</style>
</head>
<body>
<main class="canvas">

  <section class="postcard-front" aria-label="Postcard front">
    <div class="instrument-photo left" role="img" aria-label="Photograph of a silver saxophone, a trumpet and a gold alto saxophone"></div>
    <div class="instrument-photo right" role="img" aria-label="Photograph of a flute, a trombone and a clarinet"></div>
    <div class="brand-front">Marcato<br>Music Center</div>
    <h1 class="front-title">Harvey</h1>
    <p class="front-tagline">REACH YOUR FULL POTENTIAL</p>
    <p class="front-invite">It's time for the aspiring performer to take it to the next level!</p>
  </section>

  <section class="postcard-back" aria-label="Postcard back">
    <div class="brand-back">Marcato<br>Music Center</div>

    <ul class="contact-list">
      <li>
        <svg viewBox="0 0 12 12" aria-hidden="true"><path d="M6 0.5a4 4 0 0 0-4 4c0 3 4 7 4 7s4-4 4-7a4 4 0 0 0-4-4zm0 5.6a1.6 1.6 0 1 1 0-3.2 1.6 1.6 0 0 1 0 3.2z" fill="#111"/></svg>
        1420 Maple Crest Road NW, Fairview, Ohio 44120
      </li>
      <li>
        <svg viewBox="0 0 12 12" aria-hidden="true"><path d="M1 4c0-2 2-2.5 5-2.5S11 2 11 4H8.5V3h-5v1z M2.5 5h7l1 5.5h-9z" fill="#111"/><circle cx="6" cy="7.7" r="1.4" fill="#fff"/></svg>
        330-555-0147
      </li>
      <li>
        <svg viewBox="0 0 12 12" aria-hidden="true"><circle cx="6" cy="6" r="5" fill="none" stroke="#111" stroke-width="1.2"/><ellipse cx="6" cy="6" rx="2.2" ry="5" fill="none" stroke="#111" stroke-width="1"/><path d="M1 6h10" stroke="#111" stroke-width="1"/></svg>
        www.marcatomusic.com
      </li>
    </ul>

    <div class="postage-box">PRESORTED<br>STANDARD<br>US POSTAGE<br><strong>PAID</strong><br>FAIRVIEW, OH<br>PERMIT #1005</div>

    <p class="offer-copy">Your student is ready to <em>step up</em> to a Harvey Performance Instrument. To make it easier, you may apply equity from the instrument you are currently renting towards the upgraded Harvey Perfomance or Artist Series Instrument.</p>

    <p class="call-to-action">Please call to set up<br>your private appointment.</p>

    <div class="lesson-panel">
      <svg class="lesson-badge" viewBox="0 0 96 96" role="img" aria-label="We offer lessons for most instruments">
        <polygon fill="#111" points="48,2 54,8 62,4 66,11 75,10 76,18 84,20 82,28 89,33 85,40 91,47 85,54 89,61 82,66 84,74 76,76 75,84 66,83 62,90 54,86 48,92 42,86 34,90 30,83 21,84 20,76 12,74 14,66 7,61 11,54 5,47 11,40 7,33 14,28 12,20 20,18 21,10 30,11 34,4 42,8"/>
        <g fill="#fff" font-family="Jost, sans-serif" font-weight="600" font-size="8.3" text-anchor="middle" transform="rotate(-12 48 48)">
          <text x="48" y="34">WE OFFER</text>
          <text x="48" y="44">LESSONS FOR</text>
          <text x="48" y="54">MOST</text>
          <text x="48" y="64">INSTRUMENTS!</text>
        </g>
      </svg>
      <p class="lesson-headline">Large lesson studio with highly qualified instructors.</p>
      <p class="lesson-list">Lessons available for: piano, guitar, voice, drums,<br>brasswinds, woodwinds, violin, viola and cello.</p>
    </div>
  </section>

</main>
</body>
</html>
```